Simple, Professional and neat business card design for Vendralo Inc.

We're looking to re-vamp our business card design. We're a supplier of innovative feed ingredients for the North American animal agriculture industry. We are located in Lucknow, Ontario, Canada and our flagship product is a product that prevents milk fever in dairy cows when the calve, it is fed before calving and is very effective compared to other alternatives available on the market today.

Our company has Danish roots and we import all of our product from our Danish partner/manufacturer in Denmark. We like our design to embrace high professionalism while remaining neat and simple.

Target Market(s)

B2B, Feed Mills, Veterinary Clinics, Large integrators/producers,

Industry/Entity Type

Agribusiness

Contact Information for Business Card

We like the rounded corners because they make the card easy to sit in a wallet and not many use it so it makes the card stand out, just possibly something to take account for during the design.

As you can also see on the sliders below, looking for a that simple but proffesional scandinavian design.

Requirements
Nice to have
• Rounded corners
Should not have
• Too vibrant

```html
<!DOCTYPE html>
<html lang="en">
<head>
<meta charset="utf-8">
<title>Vendralo Inc. – Business Card</title>
<link href="https://fonts.googleapis.com/css2?family=Montserrat:wght@700&family=Oswald:wght@500&family=Open+Sans:wght@400;600&display=swap" rel="stylesheet">
<style>
  :root {
    --bg: #e9ebee;
    --card: #ffffff;
    --brand-blue: #1f57a8;
    --ink: #2f3133;
    --muted: #55585c;
    --map-grey: #e6e7e9;
    --rule: #9a9da1;
    --social-1: #3b5998;
    --social-2: #d9261c;
    --social-3: #4aa3df;
  }
  * { margin: 0; padding: 0; box-sizing: border-box; }
  html, body { width: 1200px; height: 1000px; overflow: hidden; }
  body {
    background: var(--bg);
    font-family: "Open Sans", sans-serif;
    position: relative;
  }
  .card {
    position: absolute;
    width: 720px;
    height: 412px;
    background: var(--card);
    border-radius: 36px;
    box-shadow: 0 10px 30px rgba(0,0,0,0.12);
    overflow: hidden;
  }
  .card--front { left: 90px; top: 60px; }
  .card--back { left: 390px; top: 528px; }

  .world-map {
    position: absolute;
    left: 40px; top: 24px;
    width: 640px; height: 364px;
    border-radius: 120px;
    background: radial-gradient(ellipse at center, var(--map-grey) 0%, rgba(230,231,233,0.6) 55%, rgba(255,255,255,0) 75%);
  }
  .brand {
    position: absolute;
    display: flex;
    align-items: center;
    gap: 18px;
  }
  .brand__mark {
    border-radius: 50%;
    background: var(--brand-blue);
    flex: none;
  }
  .brand__name {
    font-family: "Montserrat", sans-serif;
    font-weight: 700;
    color: var(--brand-blue);
    letter-spacing: 0.5px;
    white-space: nowrap;
  }
  .card--front .brand { left: 150px; top: 150px; }
  .card--front .brand__mark { width: 62px; height: 62px; }
  .card--front .brand__name { font-size: 50px; }

  .social {
    position: absolute;
    left: 50%; top: 290px;
    transform: translateX(-50%);
    display: flex; gap: 12px;
  }
  .social__dot { width: 28px; height: 28px; border-radius: 50%; }
  .social__dot--a { background: var(--social-1); }
  .social__dot--b { background: var(--social-2); }
  .social__dot--c { background: var(--social-3); }

  .card--back .brand { right: 48px; top: 36px; gap: 12px; }
  .card--back .brand__mark { width: 40px; height: 40px; }
  .card--back .brand__name { font-size: 28px; }

  .person {
    position: absolute;
    left: 50px; top: 196px;
    width: 340px;
    text-align: right;
  }
  .person__name {
    font-family: "Oswald", sans-serif;
    font-weight: 500;
    font-size: 44px;
    color: var(--ink);
    text-transform: uppercase;
    line-height: 1;
    white-space: nowrap;
    letter-spacing: 0.5px;
  }
  .person__role {
    font-size: 22px;
    font-weight: 600;
    color: var(--brand-blue);
    margin-top: 8px;
  }
  .divider {
    position: absolute;
    left: 412px; top: 124px;
    width: 2px; height: 150px;
    background: var(--rule);
  }
  .contact {
    position: absolute;
    left: 434px; top: 122px;
    list-style: none;
    font-size: 17px;
    color: var(--muted);
    line-height: 30px;
  }
  .contact li { display: flex; align-items: center; gap: 10px; white-space: nowrap; }
  .contact svg { width: 16px; height: 16px; flex: none; fill: none; stroke: var(--brand-blue); stroke-width: 2; }
  .contact .web-accent { color: var(--brand-blue); }
  .address {
    position: absolute;
    left: 60px; bottom: 42px;
    font-size: 17px;
    color: var(--muted);
  }
  .address__label { color: var(--brand-blue); }
</style>
</head>
<body>

  <section class="card card--front">
    <div class="world-map" role="img" aria-label="Faint grey world map in the background"></div>
    <div class="brand">
      <span class="brand__mark"></span>
      <span class="brand__name">VENDRALO INC.</span>
    </div>
    <div class="social" aria-label="Social media links">
      <span class="social__dot social__dot--a"></span>
      <span class="social__dot social__dot--b"></span>
      <span class="social__dot social__dot--c"></span>
    </div>
  </section>

  <section class="card card--back">
    <div class="brand">
      <span class="brand__mark"></span>
      <span class="brand__name">VENDRALO INC.</span>
    </div>

    <div class="person">
      <h1 class="person__name">Mikkel Sorensen</h1>
      <p class="person__role">Ceo &amp; Founder</p>
    </div>

    <div class="divider"></div>

    <ul class="contact">
      <li><svg viewBox="0 0 16 16"><rect x="4" y="1" width="8" height="14" rx="1.5"/></svg><span>555-014-2201</span></li>
      <li><svg viewBox="0 0 16 16"><path d="M4 2 L6 5 L5 7 Q7 10 9 11 L11 10 L14 12 L12 15 Q3 13 1 4 Z"/></svg><span>555-014-7730</span></li>
      <li><svg viewBox="0 0 16 16"><path d="M4 2 L6 5 L5 7 Q7 10 9 11 L11 10 L14 12 L12 15 Q3 13 1 4 Z"/></svg><span>800-555-0148 (toll free)</span></li>
      <li><svg viewBox="0 0 16 16"><rect x="1" y="3" width="14" height="10" rx="1"/><path d="M1 4 L8 9 L15 4"/></svg><span>mikkel@vendralo.com</span></li>
      <li><svg viewBox="0 0 16 16"><circle cx="9" cy="7" r="5"/><path d="M5 11 L1 15"/></svg><span>www.<span class="web-accent">vendralo</span>.com</span></li>
    </ul>

    <p class="address"><span class="address__label">Address:</span> Box 42, Elmbrook, Ontario Canada N0X 1A0</p>
  </section>

</body>
</html>
```